Ironvale Shift Services

We are a underground coal mining labour hire company, needing a website that links into our online payroll (www.wagetrakker.com.au) and also need to have job applications page that is a preform with drop down menu,s with answers or check boxes. We would also need a 3 tier administration access for access to different files.
We are looking for an ongoing relationship with future app integration

Reason: There are a few more designs to come and I'm out at the mine for another week

Industry/Entity Type

Coal Mining

```html
<!DOCTYPE html>
<html lang="en">
<head>
<meta charset="utf-8">
<title>Ironvale Shift Services</title>
<link href="https://fonts.googleapis.com/css2?family=PT+Sans:wght@400;700&family=Open+Sans:wght@400;600&display=swap" rel="stylesheet">
<style>
:root{
  --bar:#1c1c1c;
  --bar-edge:#2a2a2a;
  --nav-text:#e6e6e6;
  --ink:#1a1a1a;
  --body-text:#555555;
  --label:#7a7a7a;
  --field-border:#d6d6d6;
  --panel:#f6f6f6;
  --panel-border:#e2e2e2;
  --accent:#ef7a1c;
  --accent-dark:#c85e0a;
  --page:#ffffff;
}
*{box-sizing:border-box;margin:0;padding:0}
html,body{width:1062px;height:1200px;overflow:hidden}
body{position:relative;background:var(--page);font-family:"Open Sans",Arial,sans-serif;color:var(--body-text)}
.backdrop{position:absolute;left:0;top:74px;width:1062px;height:460px;background:linear-gradient(180deg,#e9e9e9 0%,#f4f4f4 50%,#ffffff 100%)}
.site-header{position:absolute;left:0;top:0;width:1062px;height:74px;background:var(--bar);border-bottom:1px solid var(--bar-edge)}
.brand{position:absolute;left:133px;top:14px;display:flex;align-items:center;gap:10px}
.brand-dot{width:44px;height:44px;border:3px solid #fff;border-radius:50%}
.brand-name{font-family:"PT Sans",sans-serif;font-weight:700;font-size:30px;color:#fff;letter-spacing:1px}
.main-nav{position:absolute;right:133px;top:28px;display:flex;gap:36px}
.main-nav a{font-family:"PT Sans",sans-serif;font-weight:700;font-size:13px;color:var(--nav-text);text-decoration:none;text-transform:uppercase}
.hero{position:absolute;left:133px;top:101px;width:796px;height:284px;border-radius:3px;overflow:hidden}
.hero-art{position:absolute;inset:0;background:linear-gradient(90deg,#0a0a0a 0%,#161616 45%,#5a5a5a 60%,#7d7d7d 80%,#4a4a4a 100%)}
.hero-circle{position:absolute;left:10px;top:-8px;width:436px;height:300px;border-radius:50%;background:radial-gradient(circle at 50% 45%,#3a2412 0%,#111 60%,#000 100%);border:3px solid #cfcfcf}
.hero-caption{position:absolute;right:22px;bottom:10px;text-align:left;color:var(--accent);font-family:"PT Sans",sans-serif}
.hero-caption .line-1{font-weight:700;font-size:29px;line-height:32px}
.hero-caption .line-2{font-family:Georgia,serif;font-size:23px;line-height:26px;color:var(--accent-dark)}
.intro{position:absolute;left:133px;top:424px;width:796px}
.intro h1,.application h2{font-family:"PT Sans",sans-serif;font-weight:700;font-size:20px;color:var(--ink)}
.intro p{margin-top:4px;font-size:12.5px;line-height:20px;color:var(--body-text)}
.application h2{position:absolute;left:133px;top:562px}
.form-panel{position:absolute;left:133px;top:598px;width:797px;height:528px;background:var(--panel);border:1px solid var(--panel-border);border-radius:4px;box-shadow:0 1px 3px rgba(0,0,0,.08);font-family:Arial,sans-serif}
.field-label{position:absolute;left:17px;font-size:12px;color:var(--label)}
.text-field{position:absolute;left:335px;width:444px;height:29px;background:#fff;border:1px solid var(--field-border);border-radius:4px}
.check{position:absolute;display:flex;align-items:center;gap:4px;font-size:11px;color:var(--label)}
.check i{display:inline-block;width:11px;height:11px;border:1px solid #b9b9b9;background:#fff}
.field-note{position:absolute;left:335px;top:168px;width:440px;font-size:9.5px;line-height:14px;color:#9a9a9a}
.select-field{position:absolute;left:335px;top:273px;width:56px;height:24px;background:#fff;border:1px solid var(--field-border);border-radius:5px;font-size:11px;color:#333;padding:5px 0 0 16px}
.select-field span{position:absolute;right:0;top:0;width:18px;height:22px;border-left:1px solid var(--field-border);font-size:8px;text-align:center;line-height:11px;padding-top:1px}
.phone-code{position:absolute;left:335px;top:432px;width:40px;height:30px;background:#fff;border:1px solid var(--field-border);border-radius:4px;font-size:12px;color:var(--label);text-align:center;line-height:28px}
.phone-field{position:absolute;top:432px;height:30px;background:#fff;border:1px solid var(--field-border);border-radius:4px}
.submit{position:absolute;left:679px;top:478px;width:100px;height:32px;background:linear-gradient(#3a3a3a,#111);border:1px solid #000;border-radius:4px;color:#fff;font-size:14px;text-align:center;line-height:30px;text-transform:uppercase}
.site-footer{position:absolute;left:0;top:1159px;width:1062px;height:41px;background:var(--bar);font-size:11.5px;color:#ddd}
.site-footer .copy{position:absolute;left:133px;top:13px}
.footer-nav{position:absolute;right:133px;top:13px;display:flex;gap:12px}
.footer-nav a{color:#eee;text-decoration:none}
</style>
</head>
<body>
<div class="backdrop" role="img" aria-label="Faint underground mine tunnel photograph behind the top of the page"></div>

<header class="site-header">
  <div class="brand"><span class="brand-dot"></span><span class="brand-name">Ironvale</span></div>
  <nav class="main-nav"><a href="#">Home</a><a href="#">About us</a><a href="#">Mission statement</a><a href="#">Contact us</a></nav>
</header>

<section class="hero">
  <div class="hero-art" role="img" aria-label="Underground coal mine tunnel with timber supports"></div>
  <div class="hero-circle" role="img" aria-label="Circular illustration of a miner with helmet and pick, Ironvale Shift Services"></div>
  <div class="hero-caption"><div class="line-1">Lorem ipsum dolor amet</div><div class="line-2">Donec fringilla tortor Morbi</div></div>
</section>

<section class="intro">
  <h1>Welcome to Ironvale</h1>
  <p>Lorem ipsum dolor sit amet, consectetur adipiscing elit. Proin a gravida sapien, vitae varius dui. In rutrum egestas magna. Fusce eu ante dignissim mi rutrum pretium sit amet quis massa. Nulla pharetra pretium libero, vitae tincidunt lorem fermentum vitae. Integer ac iaculis mi. Morbi semper est a nibh varius, ac tincidunt nisl hendrerit. Etiam aliquet, neque sit amet eleifend fermentum, nisl massa iaculis arcu, in ornare tellus erat et lorem Lorem ipsum dolor sit amet, consectetur adipiscing elit.</p>
</section>

<section class="application">
  <h2>Application for Position</h2>
  <div class="form-panel">
    <span class="field-label" style="top:17px">Do you have current Coal Boad Generics:</span>
    <div class="text-field" style="top:19px"></div>
    <span class="field-label" style="top:60px">Do you have a current Coal Board Medical:</span>
    <div class="text-field" style="top:73px"></div>

    <span class="field-label" style="top:107px">What mines are you currently inducted at:</span>
    <label class="check" style="left:335px;top:127px"><i></i>Cradle Ridge</label>
    <label class="check" style="left:423px;top:127px"><i></i>Marlow Bend</label>
    <label class="check" style="left:515px;top:127px"><i></i>Brookfield Flats</label>
    <label class="check" style="left:623px;top:127px"><i></i>Gully Creek</label>
    <label class="check" style="left:732px;top:127px"><i></i>Kestwood</label>
    <label class="check" style="left:335px;top:146px"><i></i>Oakvale North</label>
    <label class="check" style="left:423px;top:146px"><i></i>Oakvale 1</label>
    <label class="check" style="left:515px;top:146px"><i></i>Emberton</label>
    <label class="check" style="left:623px;top:146px"><i></i>Carrow Downs</label>
    <p class="field-note">These are the underground mines in queensland, there will be a list of the underground mines for new south wales as well.</p>

    <span class="field-label" style="top:223px">What mines have you been inducted at in the past:</span>
    <div class="text-field" style="top:218px"></div>

    <span class="field-label" style="top:276px">How many years underground experience do you have:</span>
    <div class="select-field">1<span>▲<br>▼</span></div>

    <span class="field-label" style="top:315px">What tickets do you have:</span>
    <label class="check" style="left:335px;top:321px"><i></i>Gopher</label>
    <label class="check" style="left:480px;top:321px"><i></i>QDS Bolter</label>
    <label class="check" style="left:589px;top:321px"><i></i>Airtrack</label>
    <label class="check" style="left:335px;top:340px"><i></i>936 or FBL 40 or similar</label>
    <label class="check" style="left:480px;top:340px"><i></i>Personnel carrier</label>
    <label class="check" style="left:589px;top:340px"><i></i>ED7/ED10 loader or similar</label>

    <span class="field-label" style="top:379px">What qualifications do you currently hold:</span>
    <label class="check" style="left:335px;top:376px"><i></i>Supervisor S1 S2 S3</label>
    <label class="check" style="left:480px;top:376px"><i></i>Trade Certificate</label>
    <label class="check" style="left:589px;top:376px"><i></i>Deputy Certificate</label>
    <label class="check" style="left:335px;top:394px"><i></i>Front line management</label>
    <label class="check" style="left:480px;top:394px"><i></i>Trainer and Assessor</label>

    <span class="field-label" style="top:438px">Contact No:</span>
    <div class="phone-code">+91</div>
    <div class="phone-field" style="left:384px;width:193px"></div>
    <div class="phone-field" style="left:586px;width:193px"></div>

    <div class="submit">Submit</div>
  </div>
</section>

<footer class="site-footer">
  <span class="copy">© 2014 ironvaleshift.com.au</span>
  <nav class="footer-nav"><a href="#">Home</a><a href="#">About Us</a><a href="#">Mission statement</a><a href="#">Contact us</a></nav>
</footer>
</body>
</html>
```